Maple Yard Fight Club's Heatwave Trim-Up Contest

Maple Yard Fight Club Presents
“The Heatwave Trim-Up Showdown”
Win the fight for fitness and take home awesome prizes.
1st Place Tabby Lite (16gb) (value $299)
2nd Place One-Month All Access Membership (value $199)
3rd Place Maple Yard Fight Club Training Gloves, T-Shirt and Handwraps (value $79)
(fine print)
* Men’s & Women’s Divisions – two sets of prizes.
* Contestants must register between June 10th and June 15th. Entry fee is $25.
* At registration, contestants will be required to weigh-in in a private setting. For the duration of the competition, actual weight will not be posted; only percent gain or loss.
* Results are based on percentage weight loss as measured on September 19th.
Note: Maple Yard Fight Club reserves the right to cancel the competition in a division if there are fewer than 10 contestants in that division. In that event, a full refund will be issued to participants in that division.

ABOUT US:
MYFC is not a traditional health club with rows of cardio equipment, weight-training machines, or overcrowded step-aerobic classes. Nor are we like old-school boxing or martial arts studios which can oftentimes be scary and uninviting.

Our goal is to strike a balance between instruction, conditioning and fun. We offer over 70 classes per week: mostly boxing, but also muay thai, mixed martial arts ("MMA"), and boot camps. All of our instructors have fought professionally or at the amateur level so they're teaching from experience, not what they learned from an online course.

Target Market(s)

Gym members.

Industry/Entity Type

Fitness

Requirements
Must have
• Our logo (attached) converted to blue.

```html
<!DOCTYPE html>
<html lang="en">
<head>
<meta charset="utf-8">
<title>Maple Yard Fight Club – Heatwave Trim-Up Contest</title>
<link href="https://fonts.googleapis.com/css2?family=Roboto+Condensed:wght@200;300;700;800;900&family=Quicksand:wght@500;600;700&family=Arimo:wght@400;700&display=swap" rel="stylesheet">
<style>
  :root{
    --page:#ffffff;
    --cream:#fbf0b7;
    --orange:#fdb870;
    --navy:#1f2d5c;
  }
  *{margin:0;padding:0;box-sizing:border-box}
  html,body{width:1200px;height:900px;overflow:hidden;background:var(--page)}
  .poster{
    position:absolute;left:237px;top:0;width:725px;height:900px;
    background:var(--cream);overflow:hidden;color:var(--navy);
  }
  .poster__curves{position:absolute;inset:0}
  .content{position:relative;text-align:center}
  .brand{
    position:absolute;left:0;right:0;top:30px;
    display:flex;justify-content:center;align-items:center;gap:8px;
    font-family:"Quicksand",sans-serif;font-weight:700;font-size:19px;line-height:1;
  }
  .brand__mark{width:12px;height:12px;background:var(--navy)}
  .presents{
    position:absolute;left:0;right:0;top:95px;
    font-family:"Quicksand",sans-serif;font-weight:600;font-size:21px;
  }
  .title{position:absolute;left:0;right:0;top:138px;font-family:"Roboto Condensed",sans-serif;text-transform:uppercase}
  .title span{display:block;line-height:1}
  .title__top{font-weight:900;font-size:100px;letter-spacing:-1px;height:116px}
  .title__middle{font-weight:200;font-size:150px;letter-spacing:-2px;height:128px;margin-top:0}
  .title__bottom{font-weight:900;font-size:142px;letter-spacing:-3px;margin-top:4px}
  .tagline{
    position:absolute;left:0;right:0;top:538px;
    font-family:"Quicksand",sans-serif;font-weight:600;font-size:32px;line-height:39px;
  }
  .prizes{position:absolute;left:90px;top:636px;list-style:none;text-align:left}
  .prize{display:flex;align-items:baseline;margin-bottom:5px}
  .prize__place{
    width:100px;flex:none;
    font-family:"Roboto Condensed",sans-serif;font-weight:800;font-size:21px;
  }
  .prize__item{font-family:"Quicksand",sans-serif;font-weight:600;font-size:16.5px;line-height:24px}
  .fine-print{
    position:absolute;left:45px;right:40px;top:783px;text-align:left;
    font-family:"Arimo",sans-serif;font-size:9.6px;line-height:12px;list-style:none;
  }
  .fine-print li{padding-left:7px;text-indent:-7px}
  .fine-print .note{padding-left:6px;text-indent:0;margin-top:4px}
</style>
</head>
<body>
<main class="poster">
  <svg class="poster__curves" width="725" height="900" viewBox="0 0 725 900" aria-hidden="true">
    <ellipse cx="-260" cy="378" rx="418" ry="420" fill="var(--orange)"/>
    <ellipse cx="985" cy="378" rx="418" ry="420" fill="var(--orange)"/>
    <rect x="0" y="755" width="725" height="145" fill="var(--cream)"/>
  </svg>
  <div class="content">
    <div class="brand"><span class="brand__mark"></span>Maple Yard Fight Club</div>
    <p class="presents">Maple Yard Fight Club Presents</p>
    <h1 class="title">
      <span class="title__top">The Heatwave</span>
      <span class="title__middle">Trim-Up</span>
      <span class="title__bottom">Showdown</span>
    </h1>
    <p class="tagline">Win the fight for fitness and take<br>home awesome prizes!</p>
    <ul class="prizes">
      <li class="prize"><span class="prize__place">1st Place</span><span class="prize__item">Tabby Lite (16gb) (value $299)</span></li>
      <li class="prize"><span class="prize__place">2nd Place</span><span class="prize__item">One-Month All Access Membership (value $199)</span></li>
      <li class="prize"><span class="prize__place">3rd Place</span><span class="prize__item">Maple Yard Fight Club Training Gloves,<br>T-Shirt and Handwraps (value $79)</span></li>
    </ul>
    <ul class="fine-print">
      <li>* Men’s &amp; Women’s Divisions – two sets of prizes.</li>
      <li>* Contestants must register between June 10th and June 15th. Entry fee is $25.</li>
      <li>* At registration, contestants will be required to weigh-in in a private setting. For the duration of the competition, actual weight will not be posted; only percent gain or loss.</li>
      <li>* Results are based on percentage weight loss as measured on September 19th.</li>
      <li class="note">Note: Maple Yard Fight Club reserves the right to cancel the competition in a division if there are fewer than 10 contestants in that division. In that event, a full refund will be issued to participants in that division.</li>
    </ul>
  </div>
</main>
</body>
</html>
```